Business Cards and Stationary for telecommunications application
BrightOak Ventures
Business Cards and Stationary for telecommunications application - Telecommunications
Creative Brief
Simple
Louis Merrow
President
20391 Kelvane Court Larkwood Ridge, OR
louis@brightoakventures.com
brightoakventures.com

```html
<!DOCTYPE html>
<html lang="en">
<head>
<meta charset="utf-8">
<title>BrightOak Ventures — Business Card</title>
<link href="https://fonts.googleapis.com/css2?family=Roboto:wght@400;500;700&display=swap" rel="stylesheet">
<style>
  :root {
    --bg: #e4e4e6;
    --card: #ffffff;
    --red: #c8161d;
    --red-dark: #8e0d12;
    --ink: #2e2e30;
    --grey: #6b6b6e;
    --black: #111111;
  }
  * { margin: 0; padding: 0; box-sizing: border-box; }
  html, body { width: 1200px; height: 984px; overflow: hidden; }
  body {
    background: var(--bg);
    font-family: "Roboto", Arial, sans-serif;
    position: relative;
  }
  .card {
    position: absolute;
    left: 250px;
    width: 700px;
    height: 400px;
    background: var(--card);
    border-radius: 22px;
    overflow: hidden;
    box-shadow: 0 10px 28px rgba(0,0,0,0.18);
  }
  .card--front { top: 52px; }
  .card--back { top: 532px; }

  .brand {
    display: flex;
    align-items: center;
    gap: 14px;
  }
  .brand__dot {
    width: 58px; height: 58px;
    border-radius: 50%;
    background: var(--red);
    flex: none;
  }
  .brand__name {
    font-size: 40px;
    font-weight: 500;
    color: var(--ink);
    letter-spacing: -0.5px;
    white-space: nowrap;
  }

  .card--front .brand {
    position: absolute;
    left: 50%; top: 140px;
    transform: translateX(-50%);
  }
  .front__web {
    position: absolute;
    left: 0; right: 0; top: 250px;
    text-align: center;
    font-size: 17px;
    letter-spacing: 4px;
    color: var(--grey);
  }

  .back__swoosh { position: absolute; inset: 0; width: 700px; height: 400px; }
  .card--back .brand {
    position: absolute;
    left: 44px; top: 150px;
  }
  .card--back .brand__dot { width: 52px; height: 52px; }
  .card--back .brand__name { font-size: 34px; }

  .person { position: absolute; left: 44px; top: 248px; }
  .person__name { font-size: 24px; font-weight: 700; color: var(--red); }
  .person__title { font-size: 18px; color: var(--grey); margin-top: 4px; }

  .contact {
    position: absolute;
    left: 430px; top: 268px;
    list-style: none;
    font-size: 13px;
    line-height: 22px;
    color: var(--grey);
  }
  .contact li { display: flex; align-items: flex-start; gap: 8px; }
  .contact__icon {
    width: 15px; height: 15px; border-radius: 50%;
    background: var(--red); flex: none; margin-top: 4px;
    display: flex; align-items: center; justify-content: center;
  }
  .contact__icon svg { width: 9px; height: 9px; }
</style>
</head>
<body>

  <section class="card card--front">
    <div class="brand">
      <span class="brand__dot"></span>
      <span class="brand__name">BrightOak Ventures</span>
    </div>
    <p class="front__web">www.brightoakventures.com</p>
  </section>

  <section class="card card--back">
    <svg class="back__swoosh" viewBox="0 0 700 400" aria-hidden="true">
      <defs>
        <linearGradient id="redSweep" x1="0" y1="0" x2="1" y2="1">
          <stop offset="0" stop-color="#8e0d12"/>
          <stop offset="0.55" stop-color="#c8161d"/>
          <stop offset="1" stop-color="#8e0d12"/>
        </linearGradient>
      </defs>
      <path d="M170,0 H700 V270 C610,130 420,40 170,0 Z" fill="url(#redSweep)"/>
      <path d="M110,14 C360,40 560,120 700,262 L700,282 C560,142 360,58 110,14 Z" fill="#111111"/>
    </svg>

    <div class="brand">
      <span class="brand__dot"></span>
      <span class="brand__name">BrightOak Ventures</span>
    </div>

    <div class="person">
      <p class="person__name">Louis Merrow</p>
      <p class="person__title">President</p>
    </div>

    <ul class="contact">
      <li>
        <span class="contact__icon"><svg viewBox="0 0 10 10"><path d="M5 0.5a3 3 0 0 1 3 3c0 2.3-3 6-3 6s-3-3.7-3-6a3 3 0 0 1 3-3z" fill="#fff"/></svg></span>
        <span>20391 Kelvane Court<br>Larkwood Ridge, OR</span>
      </li>
      <li>
        <span class="contact__icon"><svg viewBox="0 0 10 10"><path d="M2 1h2l1 2.5-1.2.8a6 6 0 0 0 2 2l.8-1.2L9 6v2c0 .6-.5 1-1 1A8 8 0 0 1 1 2c0-.5.4-1 1-1z" fill="#fff"/></svg></span>
        <span>555-014-2786</span>
      </li>
      <li>
        <span class="contact__icon"><svg viewBox="0 0 10 10"><rect x="1" y="2.5" width="8" height="5" fill="#fff"/><path d="M1 2.5l4 3 4-3" stroke="#c8161d" stroke-width="0.8" fill="none"/></svg></span>
        <span>louis@brightoakventures.com</span>
      </li>
      <li>
        <span class="contact__icon"><svg viewBox="0 0 10 10"><circle cx="5" cy="5" r="3.6" stroke="#fff" stroke-width="1" fill="none"/><path d="M1.4 5h7.2M5 1.4c1.6 2 1.6 5.2 0 7.2M5 1.4c-1.6 2-1.6 5.2 0 7.2" stroke="#fff" stroke-width="0.8" fill="none"/></svg></span>
        <span>www.brightoakventures.com</span>
      </li>
    </ul>
  </section>

</body>
</html>
```